Building/Renovation Company needs Website

I need a website designed for a renovation/building company based in Hampshire. We specialise in kitchens, bathrooms, carpentry, plastering, brickwork, ground/garden works and decorating, and all our work is fully insured and carried out to a high standard.

With the photos, display them in a before/after format.

Coding

Coded - Design and coding required

Number of Pages Required

1 page

```html
<!DOCTYPE html>
<html lang="en">
<head>
<meta charset="utf-8">
<title>Hartwell Builds – Renovation &amp; Building Specialists in Hampshire</title>
<link rel="stylesheet" href="https://fonts.googleapis.com/css2?family=Outfit:wght@300;400;500;600&display=swap">
<style>
:root{
  --navy:#283593;
  --navy-deep:#25338a;
  --lime:#d9e021;
  --ink:#1d1d1f;
  --white:#ffffff;
  --muted:#3a3a44;
}
*{box-sizing:border-box;margin:0;padding:0}
html,body{width:1200px;height:3769px;overflow:hidden;background:var(--white)}
body{position:relative;font-family:"Outfit",sans-serif;color:var(--ink)}
.abs{position:absolute}
.accent{position:absolute;background:var(--lime)}
.photo{position:absolute;overflow:hidden}
.btn{position:absolute;display:flex;align-items:center;justify-content:center;font-size:15px;font-weight:500;border-radius:5px}
.btn-lime{background:var(--lime);color:var(--navy)}
.btn-ghost{border:1.5px solid var(--lime);color:var(--lime)}
.btn-outline{border:1.5px solid var(--navy);color:var(--navy)}

/* Header */
.brand{position:absolute;display:flex;align-items:center;gap:12px}
.brand-mark{width:46px;height:46px;background:var(--lime);flex:none}
.brand-name{font-weight:500;color:var(--navy);letter-spacing:.5px;white-space:nowrap;line-height:1}
.nav{position:absolute;top:74px;left:389px;font-size:15px;color:var(--ink)}
.nav a{color:inherit;text-decoration:none;position:absolute;white-space:nowrap}
.nav .active{color:var(--navy);font-weight:500;text-decoration:underline;text-underline-offset:4px}
.location{position:absolute;left:948px;top:73px;display:flex;align-items:center;gap:10px;font-size:15px;font-weight:600;color:var(--ink)}

/* Hero & CTA */
.banner-text{position:absolute;color:var(--white)}
.eyebrow{font-size:30px;font-weight:400}
.display{font-size:55px;font-weight:500;line-height:56px}
.display .lime{color:var(--lime)}
.lead{font-size:16px;line-height:26px}

/* About */
.kicker{font-size:21px;font-weight:400;color:var(--ink)}
.heading{font-size:39px;font-weight:500;line-height:46px;color:var(--navy)}
.heading .lime{color:var(--lime)}
.bullets{list-style:none;font-size:15px;line-height:26px;color:var(--muted)}
.bullets li{position:relative;margin-bottom:17px}
.bullets li::before{content:"";position:absolute;left:-20px;top:9px;width:7px;height:7px;background:var(--lime)}
.bullets strong{color:var(--navy);font-weight:500}

/* Services */
.services{position:absolute;left:0;top:1362px;width:1200px;height:922px;background:var(--navy)}
.services .kicker{color:var(--white)}
.services .heading{color:var(--white)}
.card-title{position:absolute;font-size:31px;font-weight:400;color:var(--white);white-space:nowrap}
.card-title.lime{color:var(--lime)}
.feature{position:absolute;top:652px;width:322px;height:167px;border:1.5px solid var(--lime)}
.feature h3{position:absolute;left:94px;top:24px;font-size:22px;font-weight:400;color:var(--lime)}
.feature p{position:absolute;left:95px;top:64px;width:200px;font-size:15px;line-height:26px;color:var(--white)}
.feature svg{position:absolute;left:24px;top:22px}

/* Portfolio */
.project-panel{position:absolute;left:54px;top:2687px;width:504px;height:237px;background:var(--navy)}
.project-panel h3{position:absolute;left:56px;top:34px;font-size:31px;font-weight:400;color:var(--lime)}
.project-panel p{position:absolute;left:56px;top:82px;width:400px;font-size:15px;line-height:26px;color:var(--white)}
.ba-label{position:absolute;top:2868px;font-size:21px;color:var(--navy)}

/* Footer */
.footer-copy{position:absolute;font-size:15px;line-height:26px;color:var(--ink)}
.contact-item{position:absolute;top:3641px;display:flex;align-items:center;gap:10px;font-size:15px;color:var(--ink)}
.social{position:absolute;top:3701px;left:758px;display:flex;gap:14px}
.social span{width:20px;height:20px;border-radius:50%;background:var(--lime)}
</style>
</head>
<body>

<!-- Header -->
<header>
  <div class="brand" style="left:110px;top:58px;gap:10px">
    <div class="brand-mark" style="width:40px;height:40px"></div>
    <div class="brand-name" style="font-size:20px">HARTWELL BUILDS</div>
  </div>
  <nav class="nav">
    <a class="active" style="left:0">HOME</a>
    <a style="left:91px">ABOUT</a>
    <a style="left:185px">SERVICES</a>
    <a style="left:300px">PORTFOLIO</a>
    <a style="left:429px">CONTACT</a>
  </nav>
  <div class="location">
    <svg width="14" height="18" viewBox="0 0 14 18"><path d="M7 0a7 7 0 0 0-7 7c0 5 7 11 7 11s7-6 7-11a7 7 0 0 0-7-7z" fill="var(--lime)"/><circle cx="7" cy="7" r="2.6" fill="#fff"/></svg>
    HAMPSHIRE, UK
  </div>
</header>

<!-- Hero -->
<section>
  <div class="accent" style="left:82px;top:150px;width:46px;height:305px;clip-path:polygon(0 0,100% 8%,100% 100%,0 94%)"></div>
  <div class="accent" style="left:1056px;top:373px;width:46px;height:305px;clip-path:polygon(0 6%,100% 0,100% 100%,0 94%)"></div>
  <div class="photo" role="img" aria-label="Renovated kitchen with dark cabinets, wooden worktop and sink beneath a window" style="left:111px;top:171px;width:978px;height:486px;background:linear-gradient(110deg,#17181d 0%,#2a2c33 45%,#5a5e66 70%,#8d9298 100%)"></div>
  <div class="banner-text" style="left:189px;top:254px">
    <div class="eyebrow">Hartwell Builds</div>
    <div class="display" style="margin-top:8px"><span class="lime">Renovation &amp; Building</span><br>Specialists in Hampshire</div>
    <p class="lead" style="margin-top:20px">Transforming homes across Hampshire with high-quality renovations,<br>expert craftsmanship, and a friendly, reliable service.</p>
  </div>
  <a class="btn btn-lime" style="left:190px;top:521px;width:207px;height:44px">Request a Free Quote</a>
  <a class="btn btn-ghost" style="left:407px;top:521px;width:154px;height:44px">View Projects</a>
</section>

<!-- About -->
<section>
  <div class="accent" style="left:92px;top:849px;width:19px;height:417px;clip-path:polygon(0 4%,100% 0,100% 100%,0 100%)"></div>
  <div class="accent" style="left:527px;top:773px;width:18px;height:410px;clip-path:polygon(0 2%,100% 0,100% 97%,0 100%)"></div>
  <div class="photo" role="img" aria-label="White rendered terraced house rear with prepared garden ground and timber fences" style="left:111px;top:783px;width:416px;height:471px;background:linear-gradient(180deg,#9aa0a8 0%,#d9d9d6 35%,#bdb9b1 55%,#4d4640 75%,#3b342e 100%)"></div>
  <div class="kicker abs" style="left:632px;top:816px">Who We Are</div>
  <h2 class="heading abs" style="left:632px;top:854px">Quality Renovations<br><span class="lime">Trusted Local Team</span></h2>
  <ul class="bullets abs" style="left:632px;top:970px;width:460px">
    <li><strong>Hartwell Builds</strong> was created to offer homeowners a straightforward, trustworthy renovation service with a focus on quality finishes and practical design.</li>
    <li>The team brings together experienced tradespeople who all specialise in kitchens, bathrooms, carpentry, plastering, brickwork, ground and garden works, and decorating.</li>
  </ul>
  <a class="btn btn-outline" style="left:632px;top:1175px;width:210px;height:44px">Learn More About Us</a>
</section>

<!-- Services -->
<section class="services">
  <div class="kicker abs" style="left:111px;top:103px">Our Services</div>
  <h2 class="heading abs" style="left:111px;top:140px">Comprehensive<br><span class="lime">Renovation Services</span></h2>
  <p class="abs lead" style="left:632px;top:151px;width:470px;color:var(--white);font-size:15px">Transform your home with expert kitchen, bathroom, carpentry, plastering, brickwork, ground and garden works, and decor services – all delivered by a fully insured, professional team.</p>

  <div class="accent" style="left:102px;top:280px;width:25px;height:292px;clip-path:polygon(0 0,100% 8%,100% 100%,0 100%)"></div>
  <div class="card-title lime" style="left:155px;top:295px">1. Kitchen Renovation</div>
  <div class="card-title" style="left:588px;top:295px">2. Ground / Garden Work</div>
  <div class="card-title" style="left:1032px;top:295px;opacity:.8">3. Bathroom</div>

  <div class="photo" role="img" aria-label="Finished kitchen with grey units, tiled splashback and oven" style="left:111px;top:356px;width:416px;height:228px;border:2px solid var(--lime);background:linear-gradient(120deg,#2e3038 0%,#4a4d55 45%,#8c8677 70%,#c9c5bd 100%)">
    <span class="btn btn-lime" style="left:44px;top:158px;width:146px;height:42px">View Details</span>
  </div>
  <div class="accent" style="left:552px;top:356px;width:8px;height:228px"></div>
  <div class="photo" role="img" aria-label="Garden ground works with levelled soil between timber fences" style="left:560px;top:356px;width:416px;height:228px;background:linear-gradient(180deg,#b9b8b4 0%,#d8d6d1 35%,#5a5149 65%,#3d362f 100%)"></div>
  <div class="accent" style="left:1000px;top:356px;width:10px;height:228px"></div>
  <div class="photo" role="img" aria-label="Refitted bathroom with white suite and chequered floor" style="left:1010px;top:356px;width:190px;height:228px;background:linear-gradient(180deg,#8791b8 0%,#b9bfd6 55%,#3d4470 100%)">
    <svg class="abs" style="left:112px;top:98px" width="38" height="28" viewBox="0 0 38 28"><path d="M2 14h32M22 3l12 11-12 11" fill="none" stroke="var(--lime)" stroke-width="3"/></svg>
  </div>

  <div class="feature" style="left:111px">
    <svg width="46" height="56" viewBox="0 0 46 56"><path d="M23 2L3 9v17c0 14 9 23 20 28 11-5 20-14 20-28V9z" fill="none" stroke="var(--lime)" stroke-width="2.5"/><path d="M14 28l7 7 12-13" fill="none" stroke="var(--lime)" stroke-width="2.5"/></svg>
    <h3>Fully Insured</h3>
    <p>Complete peace of mind with full insurance covered on every project.</p>
  </div>
  <div class="feature" style="left:439px">
    <svg width="46" height="56" viewBox="0 0 46 56"><path d="M23 2L3 9v17c0 14 9 23 20 28 11-5 20-14 20-28V9z" fill="none" stroke="var(--lime)" stroke-width="2.5"/><path d="M23 16l3.5 7.5 8 .8-6 5.4 1.8 7.8L23 33.5l-7.3 4 1.8-7.8-6-5.4 8-.8z" fill="var(--lime)"/></svg>
    <h3>High Standards</h3>
    <p>Premium craftsmanship and finishes that stand the test of time.</p>
  </div>
  <div class="feature" style="left:767px">
    <svg width="46" height="56" viewBox="0 0 46 56"><path d="M23 2L3 9v17c0 14 9 23 20 28 11-5 20-14 20-28V9z" fill="none" stroke="var(--lime)" stroke-width="2.5"/><path d="M23 38s-10-6-10-13a5 5 0 0 1 10-2 5 5 0 0 1 10 2c0 7-10 13-10 13z" fill="var(--lime)"/></svg>
    <h3>Trusted Quality</h3>
    <p>Professional delivery from experienced Hampshire tradespeople.</p>
  </div>
</section>

<!-- Portfolio -->
<section>
  <div class="kicker abs" style="left:111px;top:2388px">Our Portfolio</div>
  <h2 class="heading abs" style="left:111px;top:2426px">Proven Transformations<br><span class="lime">Expert Craftsmanship</span></h2>
  <ul class="bullets abs" style="left:112px;top:2541px;width:450px">
    <li>Explore Hartwell Builds' transformations in kitchens, bathrooms, and outdoor spaces across Hampshire.</li>
    <li>Every project is completed to a high standard with quality materials, and craftsmanship you can see in the details.</li>
  </ul>
  <div class="project-panel">
    <h3>Bathroom Refurbishment</h3>
    <p>Complete overhaul from outdated to spa-like luxury with tiling and fittings for a modern feel.</p>
    <span class="btn btn-lime" style="left:59px;top:169px;width:198px;height:42px">View More Projects</span>
    <svg class="abs" style="left:372px;top:176px" width="30" height="22" viewBox="0 0 30 22"><path d="M28 11H3M12 2L3 11l9 9" fill="none" stroke="#8d96c8" stroke-width="2"/></svg>
    <svg class="abs" style="left:424px;top:176px" width="30" height="22" viewBox="0 0 30 22"><path d="M2 11h25M18 2l9 9-9 9" fill="none" stroke="var(--lime)" stroke-width="2.5"/></svg>
  </div>

  <div class="accent" style="left:651px;top:2363px;width:21px;height:490px;clip-path:polygon(0 0,100% 3%,100% 100%,0 100%)"></div>
  <div class="accent" style="left:1087px;top:2444px;width:18px;height:410px;clip-path:polygon(0 0,100% 4%,100% 97%,0 100%)"></div>
  <div class="photo" role="img" aria-label="Bathroom before refurbishment with white tiles, old toilet and laminate floor" style="left:672px;top:2375px;width:206px;height:473px;background:linear-gradient(180deg,#e9e7e2 0%,#d8d5cf 55%,#b79a75 78%,#a07e57 100%)"></div>
  <div class="photo" role="img" aria-label="Bathroom after refurbishment with new window, white suite and black and white chequered floor" style="left:880px;top:2375px;width:207px;height:473px;background:linear-gradient(180deg,#d6d3cf 0%,#eceae6 50%,#555 70%,#2a2a2a 100%)"></div>
  <div class="abs" style="left:877px;top:2375px;width:3px;height:473px;background:var(--white)"></div>
  <div class="abs" style="left:840px;top:2798px;width:76px;height:26px;border-radius:13px;background:var(--white);display:flex;align-items:center;justify-content:center;gap:18px">
    <svg width="8" height="10" viewBox="0 0 8 10"><path d="M7 0L0 5l7 5z" fill="var(--navy)"/></svg>
    <svg width="8" height="10" viewBox="0 0 8 10"><path d="M1 0l7 5-7 5z" fill="var(--navy)"/></svg>
  </div>
  <div class="ba-label" style="left:741px">Before</div>
  <div class="ba-label" style="left:955px">After</div>
</section>

<!-- Call to action -->
<section>
  <div class="accent" style="left:84px;top:3190px;width:46px;height:265px;clip-path:polygon(0 10%,100% 0,100% 100%,0 100%)"></div>
  <div class="accent" style="left:1056px;top:3020px;width:46px;height:290px;clip-path:polygon(0 8%,100% 0,100% 92%,0 100%)"></div>
  <div class="photo" role="img" aria-label="Rooftop timber decking terrace with outdoor furniture and tiled roofs" style="left:111px;top:3044px;width:978px;height:396px;background:linear-gradient(160deg,#3b342f 0%,#5c5147 40%,#8a5a48 60%,#3a3129 100%)"></div>
  <div class="banner-text" style="left:189px;top:3108px">
    <div class="eyebrow" style="font-size:22px">Get in Touch</div>
    <div class="display" style="font-size:39px;line-height:46px;margin-top:6px">Request a Free Quote<br><span class="lime">Let's Talk</span></div>
    <p class="lead" style="margin-top:14px;font-size:15px">Tell us about your project and we'll get back to you<br>with a no-obligation quote.</p>
  </div>
  <a class="btn btn-lime" style="left:190px;top:3331px;width:207px;height:44px">Request a Free Quote</a>
</section>

<!-- Footer -->
<footer>
  <div class="brand" style="left:117px;top:3570px;gap:16px">
    <div class="brand-mark" style="width:64px;height:64px"></div>
    <div class="brand-name" style="font-size:34px">HARTWELL BUILDS</div>
  </div>
  <p class="footer-copy" style="left:642px;top:3560px;width:440px">Transforming homes across Hampshire with high-quality renovations ,craftsmanship, and a friendly, reliable service.</p>
  <div class="contact-item" style="left:643px">
    <svg width="18" height="14" viewBox="0 0 18 14"><rect x="1" y="1" width="16" height="12" fill="none" stroke="var(--navy)" stroke-width="1.5"/><path d="M1 1l8 7 8-7" fill="none" stroke="var(--navy)" stroke-width="1.5"/></svg>
    hello@hartwellbuilds.co.uk
  </div>
  <div class="contact-item" style="left:917px">
    <svg width="16" height="16" viewBox="0 0 16 16"><path d="M3 1l3 3-1.5 2.5a9 9 0 0 0 5 5L12 10l3 3-2 2C7 15 1 9 1 3z" fill="none" stroke="var(--navy)" stroke-width="1.5"/></svg>
    07 700 900412
  </div>
  <div class="footer-copy" style="left:114px;top:3697px;color:var(--navy)">©2025 Hartwell Builds. All Rights Reserved.</div>
  <div class="footer-copy" style="left:642px;top:3694px;font-size:21px;color:var(--navy)">Follow us</div>
  <div class="social"><span></span><span></span><span></span><span></span></div>
</footer>

</body>
</html>
```